Boutique investment company is looking for money

We, Cardelith, are a very small boutique consulting and investment management firm in SWITZERLAND. Cardelith is trying to raise EUR 5-15 million in areas not easily accessible to private investors.

It will not be possible to raise these funds from traditional institutional investors because:
- Time and budget constraints
- Lack of track record in this particular area
Therefore, the capital has to be raised from in a non-conventional way, guerilla-style, from probably 10-15 private investors providing 1 million each. What can we offer? First, the money will be in Switzerland. Second, it will not be with a large bank – so, discretion is guaranteed. We are no-bullshit but data-driven, out of the box investors. We are different.

The site is only the bait to contact us. Maybe it should look like a presentation, just with additional elements for navigation. Maybe there should be one image or a chart explaining each page.

The site will be small, five pages, in two or three languages each.

Investors in Russia and South America

Boutique

Coded - Design and coding required

4 page

• Read the "Nice to Haves" section

Requirements
Must have
• If you have local insight to Russia and Southern America - use it.
• I am German and I love modern architecture - and I would like to see simple and logical design, including easy navigation.
• I am enclosing some files you may find useful. The graphics need to be consistent and can either be clean like they are now or look improvised and hand-drawn - if you can turn them consistently into that.
• We need a home page that should simply state "Safe, secure, Swiss" and then four pages: About Cardelith, Investment opportunity, Absolute return investing,
• Investment strategy. And the navigation needs to allow to toggle between English, Russian and Spanish.
• Let me help you by providing some examples of the kind of site that I have in mind, crisp, clean, simple (the sites are listed in alphabetical order):
• vemoridge.example
• tulsenfield.example
• quorvanholt.example
• zepharlind.example
• dormivelleco.example
• ketraholm.example
• lurovaspring.example
• pelmorath.example
• wistegrove.example
• fendralwick.example
• orbesquay.example
• jyn-halcrest.example
• Take a look at these and your job will become easier, much easier. They all have the same type of look and feel to them.
• One really cool landing page is here:
• wdlt.example
• Maybe we can do something like on their landing page in our logo with ursae minoris (see pictures)?
• If you use pictures, think Switzerland. Google the following and look at images:
• Matterhorn
• luzern vierwaldstättersee
• mechanical swiss watch
• vault
Nice to have
• Please look at the logo. I like the Sans Serif Fonts, Gill Sans and Helvetica Neue above all. Colors based on the logo are:
• - dark blue R: 0, G: 22, B: 115
• - light blue R: 68, G: 133, B: 212
Should not have
• Unless you feel that the audience loves pompous design, let's keep it straight.

```html
<!DOCTYPE html>
<html lang="en">
<head>
<meta charset="utf-8">
<title>Cardelith — Safe, Secure, Swiss</title>
<link rel="stylesheet" href="https://fonts.googleapis.com/css2?family=Open+Sans:wght@400;600;700&family=Roboto+Condensed:wght@400;700&display=swap">
<style>
:root{
  --navy:#001673;
  --navy-deep:#00104f;
  --sky:#4485d4;
  --ink:#333;
  --muted:#777;
  --paper:#fff;
  --mist:#eef1f5;
  --red:#e0302b;
  --green:#3aa64a;
  --footer:#0b0f1e;
}
*{margin:0;padding:0;box-sizing:border-box}
html,body{width:673px;height:1200px;overflow:hidden;background:var(--paper);font-family:"Open Sans",Arial,sans-serif;color:var(--ink)}
.page{position:relative;width:673px;height:1200px}

/* header */
.site-header{position:absolute;top:0;left:0;width:673px;height:40px;z-index:2}
.brand{position:absolute;left:34px;top:4px;background:var(--paper);padding:10px 14px 10px 12px;display:flex;align-items:center;gap:6px;box-shadow:0 2px 4px rgba(0,0,0,.15)}
.brand-dot{width:12px;height:12px;border-radius:50%;background:var(--sky)}
.brand-name{font-family:"Roboto Condensed",sans-serif;font-weight:700;font-size:20px;color:var(--navy)}
.main-nav{position:absolute;left:240px;top:0;width:316px;height:24px;display:flex;align-items:center;justify-content:space-between;background:rgba(0,16,79,.88);padding:0 9px}
.main-nav a{color:#fff;font-size:5.8px;text-decoration:none;text-transform:uppercase;white-space:nowrap}
.lang{position:absolute;left:564px;top:0;background:var(--navy);color:#fff;font-size:6.5px;padding:2px 8px;line-height:9px}

/* hero */
.hero{position:absolute;top:24px;left:0;width:673px;height:346px;background:linear-gradient(90deg,#b9b2a6 0%,#e6d8cf 30%,#c95a55 52%,#e8e2da 70%,#a88f6c 100%)}
.arrow{position:absolute;top:160px;width:20px;height:34px}
.arrow.left{left:128px}.arrow.right{right:128px}

/* intro band */
.intro{position:absolute;top:370px;left:0;width:673px;height:135px;background:var(--navy);text-align:center;color:#fff}
.intro p{font-family:"Roboto Condensed",sans-serif;font-size:19px;line-height:24px;padding-top:24px}
.btn-join{display:inline-block;margin-top:12px;border:2px solid #fff;padding:6px 18px;font-family:"Roboto Condensed",sans-serif;font-size:15px;font-weight:700;color:#fff;text-decoration:none}

/* offer strip */
.offer{position:absolute;top:505px;left:0;width:673px;height:150px;background:linear-gradient(180deg,#dde3ea,#f4f6f8)}
.offer-visual{position:absolute;top:0;height:150px}
.offer-visual.room{left:0;width:202px;background:linear-gradient(135deg,#c9d0d8,#f2f4f6)}
.offer-visual.handshake{left:202px;width:204px;background:linear-gradient(135deg,#5b8ec6,#d8e4ef)}
.offer-visual.calc{left:406px;width:267px;background:linear-gradient(135deg,#8aa7c7,#e4ebf2)}
.offer-card{position:absolute;left:70px;top:8px;width:120px;height:120px;border-radius:50%;background:var(--paper);box-shadow:0 2px 8px rgba(0,0,0,.2);text-align:center;padding-top:24px}
.offer-card h2{font-family:"Roboto Condensed",sans-serif;font-size:15px;color:var(--navy);line-height:16px}
.offer-card p{font-size:5px;color:var(--sky);width:84px;margin:8px auto 0;line-height:7px}
.dots{position:absolute;left:200px;top:136px;display:flex;gap:4px}
.dots i{width:5px;height:5px;border-radius:50%;background:#9bb}
.dots i.on{background:var(--sky)}
.pin{position:absolute;top:66px;width:0;height:0;border-left:7px solid transparent;border-right:7px solid transparent;border-top:9px solid var(--navy)}

/* safe section */
.safe{position:absolute;top:670px;left:0;width:673px;height:230px}
.safe-copy{position:absolute;left:134px;top:8px;width:198px}
.safe-copy h1{font-family:"Roboto Condensed",sans-serif;font-size:20px;font-weight:700}
.safe-copy h1 .r{color:var(--red)}.safe-copy h1 .b{color:var(--navy)}.safe-copy h1 .g{color:var(--green)}
.rule{height:1px;background:#ccc;margin:6px 0 8px}
.safe-copy p{font-size:5.6px;line-height:8px;color:var(--muted);margin-bottom:7px;text-align:justify}
.chart{position:absolute;left:346px;top:4px}

/* what we do */
.what{position:absolute;top:905px;left:0;width:673px;height:240px;background:linear-gradient(180deg,#0b2a78,var(--navy-deep))}
.what h2{position:absolute;left:132px;top:14px;font-family:"Roboto Condensed",sans-serif;font-size:22px;color:#fff}
.what-line{position:absolute;left:132px;top:42px;width:410px;height:1px;background:rgba(255,255,255,.3)}
.what-intro{position:absolute;left:132px;top:50px;width:410px;font-size:5.2px;line-height:7.5px;color:#c9d3ea;text-align:justify}
.cards{position:absolute;left:132px;top:98px;display:flex;gap:8px}
.card{width:131px}
.card .img{height:54px}
.card .cap{background:var(--paper);color:var(--navy);font-size:6px;font-weight:700;padding:4px 5px}
.card p{font-size:5px;line-height:7px;color:#c9d3ea;margin-top:5px}

/* footer */
.site-footer{position:absolute;top:1145px;left:0;width:673px;height:55px;background:var(--footer);color:#aaa}
.foot-nav{position:absolute;left:134px;top:16px;display:flex;gap:10px}
.foot-nav a{color:#ccc;font-size:5.5px;text-decoration:none;text-transform:uppercase}
.copyright{position:absolute;left:134px;top:30px;font-size:5px;color:#777}
.follow{position:absolute;left:487px;top:12px;font-size:5.5px;color:var(--sky)}
.social{position:absolute;left:487px;top:24px;display:flex;gap:3px}
.social i{width:7px;height:7px;border-radius:50%;background:var(--sky)}
</style>
</head>
<body>
<div class="page">

  <div class="hero" role="img" aria-label="Photo of women shopping for fashion in a boutique"></div>
  <svg class="arrow left" viewBox="0 0 20 34"><path d="M16 2 L4 17 L16 32" fill="none" stroke="#fff" stroke-width="3"/></svg>
  <svg class="arrow right" viewBox="0 0 20 34"><path d="M4 2 L16 17 L4 32" fill="none" stroke="#fff" stroke-width="3"/></svg>

  <header class="site-header">
    <div class="brand"><span class="brand-dot"></span><span class="brand-name">Cardelith</span></div>
    <nav class="main-nav">
      <a href="#">Home</a><a href="#">About us</a><a href="#">Investment opportunity</a><a href="#">Absolute return investing</a><a href="#">Contact</a>
    </nav>
    <span class="lang">English</span>
  </header>

  <section class="intro">
    <p>The work we have completed<br>allow us the position ourselves as experts in business</p>
    <a class="btn-join" href="#">JOIN US!</a>
  </section>

  <section class="offer">
    <div class="offer-visual room" role="img" aria-label="Bright modern interior"></div>
    <div class="offer-visual handshake" role="img" aria-label="Business handshake"></div>
    <div class="offer-visual calc" role="img" aria-label="Calculator on financial papers"></div>
    <span class="pin" style="left:195px"></span>
    <span class="pin" style="left:399px"></span>
    <div class="offer-card">
      <h2>What<br>can we offer?</h2>
      <p>Your capital stays in Switzerland, held away from large banks, with full discretion and data-driven care.</p>
    </div>
    <div class="dots"><i class="on"></i><i></i><i></i></div>
  </section>

  <section class="safe">
    <div class="safe-copy">
      <h1><span class="r">Safe,</span> <span class="b">Secure,</span> <span class="g">Swiss</span></h1>
      <div class="rule"></div>
      <p>We are a small boutique consulting and investment management firm based in Switzerland. We open areas not easily accessible to private investors, working with a focused circle of partners who value discretion, clear data and a steady long-term view over noise and short-term fashion.</p>
      <p>Our approach is independent and data-driven. Capital remains in Switzerland, outside large banking groups, and every decision follows tested models and strict risk limits so returns stay robust across changing markets and conditions.</p>
    </div>
    <svg class="chart" width="196" height="140" viewBox="0 0 196 140" font-family="Open Sans, sans-serif" font-size="5" fill="#666">
      <g stroke="#ddd" stroke-width=".6">
        <line x1="24" y1="6" x2="190" y2="6"/><line x1="24" y1="22" x2="190" y2="22"/><line x1="24" y1="38" x2="190" y2="38"/>
        <line x1="24" y1="54" x2="190" y2="54"/><line x1="24" y1="70" x2="190" y2="70"/><line x1="24" y1="86" x2="190" y2="86"/><line x1="24" y1="102" x2="190" y2="102"/>
      </g>
      <g text-anchor="end">
        <text x="21" y="8">120%</text><text x="21" y="24">100%</text><text x="21" y="40">80%</text><text x="21" y="56">60%</text>
        <text x="21" y="72">40%</text><text x="21" y="88">20%</text><text x="21" y="104">0%</text>
      </g>
      <polyline fill="none" stroke="#2c4fa3" stroke-width="1.2" points="26,100 40,96 54,92 68,88 82,80 96,84 110,74 124,66 138,62 152,56 166,50 178,34 188,20"/>
      <polyline fill="none" stroke="#9ab4de" stroke-width="1.2" points="26,101 40,98 54,96 68,92 82,90 96,88 110,84 124,80 138,76 152,72 166,66 178,60 188,52"/>
      <g transform="translate(0,108)" font-size="4.5">
        <text transform="translate(28,0) rotate(50)">Jan-12</text><text transform="translate(42,0) rotate(50)">Mar-12</text>
        <text transform="translate(56,0) rotate(50)">May-12</text><text transform="translate(70,0) rotate(50)">Jul-12</text>
        <text transform="translate(84,0) rotate(50)">Sep-12</text><text transform="translate(98,0) rotate(50)">Nov-12</text>
        <text transform="translate(112,0) rotate(50)">Jan-13</text><text transform="translate(126,0) rotate(50)">Mar-13</text>
        <text transform="translate(140,0) rotate(50)">May-13</text><text transform="translate(154,0) rotate(50)">Jul-13</text>
        <text transform="translate(168,0) rotate(50)">Sep-13</text><text transform="translate(182,0) rotate(50)">Nov-13</text>
      </g>
      <line x1="60" y1="136" x2="70" y2="136" stroke="#9ab4de" stroke-width="1.2"/><text x="72" y="138">Managed Futures</text>
      <line x1="120" y1="136" x2="130" y2="136" stroke="#2c4fa3" stroke-width="1.2"/><text x="132" y="138">Trading System</text>
    </svg>
  </section>

  <section class="what">
    <h2>What We Do</h2>
    <div class="what-line"></div>
    <p class="what-intro">We source, test and manage absolute return strategies for a small group of private investors. Each mandate is built around transparent data, Swiss custody and personal contact with the people managing your capital. We combine systematic trading, managed futures and careful research to seek steady growth with low correlation to traditional markets, keeping costs lean and reporting simple, timely and clear for every partner we serve.</p>
    <div class="cards">
      <div class="card">
        <div class="img" role="img" aria-label="City skyline" style="background:linear-gradient(135deg,#c9a27a,#6f8fb8)"></div>
        <div class="cap">Long-term capital growth built on data</div>
        <p>Steady strategies designed for private investors seeking discreet Swiss management.</p>
      </div>
      <div class="card">
        <div class="img" role="img" aria-label="Banknotes and coins" style="background:linear-gradient(135deg,#d8b56a,#a46f3c)"></div>
        <div class="cap">Absolute return with strict risk limits</div>
        <p>Tested models that aim for positive results across rising and falling markets.</p>
      </div>
      <div class="card">
        <div class="img" role="img" aria-label="Office meeting" style="background:linear-gradient(135deg,#b9c7d6,#5d7aa3)"></div>
        <div class="cap">Personal contact and clear reporting</div>
        <p>Direct access to the team, with simple reports delivered on a regular schedule.</p>
      </div>
    </div>
  </section>

  <footer class="site-footer">
    <nav class="foot-nav">
      <a href="#">Home</a><a href="#">About us</a><a href="#">Investment opportunity</a><a href="#">Absolute return investing</a><a href="#">Contact</a>
    </nav>
    <p class="copyright">© Cardelith. All rights reserved.</p>
    <span class="follow">Follow us</span>
    <div class="social"><i></i><i></i><i></i><i></i><i></i></div>
  </footer>

</div>
</body>
</html>
```